I would like a business card to match my truck wrap and logo. I would like the font to match my existing business card please.

Industry/Entity Type

Painter

Contact Information for Business Card

Rodrigo Venaza 801-437-2916 Venazacoatings.utah@brushmail.net
SERVICES - Custom Paint & Stain, Interior & Exterior, Epoxy Coatings / Garage Floors, Cabinet Refinishing, Log Staining and Refinishing.

Requirements
Nice to have
• I would like to have the white and grey line like the bottom of my vehicle wrap, Light Grey to match my truck also.

```html
<!DOCTYPE html>
<html lang="en">
<head>
<meta charset="utf-8">
<title>Venaza Coatings – Business Card</title>
<link rel="stylesheet" href="https://fonts.googleapis.com/css2?family=Arimo:wght@400;700&display=swap">
<style>
  :root {
    --canvas: #2b2e33;
    --card-white: #f7f7f7;
    --band-grey: #d9d9d9;
    --band-light: #e6e6e6;
    --line-grey: #c6c6c6;
    --brand-blue: #1ba3e6;
    --text-dark: #2a2a2a;
    --text-grey: #7d7d7d;
    --card-black: #121212;
    --stripe-dark: #3a3a3a;
    --stripe-mid: #5a5a5a;
    --stripe-base: #2a2a2a;
  }
  * { margin: 0; padding: 0; box-sizing: border-box; }
  ul { list-style: none; }
  html, body { width: 1200px; height: 800px; overflow: hidden; }
  body {
    background: var(--canvas);
    font-family: "Arimo", Arial, sans-serif;
    display: flex;
    align-items: center;
    justify-content: center;
    gap: 40px;
  }
  .card {
    position: relative;
    width: 560px;
    height: 320px;
    border-radius: 4px;
    overflow: hidden;
    box-shadow: 0 14px 30px rgba(0,0,0,0.45);
    flex-shrink: 0;
  }
  .card__bands { position: absolute; inset: 0; width: 100%; height: 100%; }

  .brand {
    position: absolute;
    display: flex;
    align-items: center;
    gap: 12px;
    color: var(--brand-blue);
    font-weight: 700;
    text-transform: uppercase;
    letter-spacing: 0.08em;
    white-space: nowrap;
  }
  .brand__mark { background: var(--brand-blue); border-radius: 4px; flex-shrink: 0; }

  /* Front */
  .card--front { background: var(--card-white); }
  .card--front .brand { top: 36px; right: 40px; font-size: 24px; }
  .card--front .brand__mark { width: 42px; height: 42px; }

  .contact {
    position: absolute;
    left: 34px;
    top: 112px;
    display: flex;
    flex-direction: column;
    gap: 12px;
  }
  .contact__item {
    display: flex;
    align-items: center;
    gap: 12px;
    font-size: 12px;
    color: var(--text-dark);
    white-space: nowrap;
  }
  .contact__icon {
    width: 30px; height: 30px;
    border-radius: 50%;
    background: var(--brand-blue);
    display: flex; align-items: center; justify-content: center;
    flex-shrink: 0;
  }

  .services {
    position: absolute;
    right: 12px;
    top: 182px;
    width: 210px;
  }
  .services__title {
    color: var(--brand-blue);
    font-size: 12px;
    font-weight: 400;
    letter-spacing: 0.25em;
    text-align: center;
    padding-bottom: 3px;
    border-bottom: 1.5px solid var(--brand-blue);
    width: 120px;
    margin: 0 auto 8px;
  }
  .services__cols {
    display: flex;
    justify-content: space-between;
    gap: 6px;
    font-size: 8.5px;
    line-height: 1.6;
    color: var(--text-grey);
    white-space: nowrap;
  }
  .services__col--left { padding-top: 14px; }
  .services__col--right { text-align: right; }

  /* Back */
  .card--back { background: var(--card-black); }
  .card--back .brand {
    top: 46%; left: 50%;
    transform: translate(-50%, -50%);
    font-size: 34px;
    gap: 16px;
  }
  .card--back .brand__mark { width: 56px; height: 56px; }
</style>
</head>
<body>

  <section class="card card--front" aria-label="Business card front">
    <svg class="card__bands" viewBox="0 0 560 320" aria-hidden="true">
      <path d="M0,262 L285,262 L335,172 L560,172 V320 H0 Z" fill="var(--band-grey)"/>
      <path d="M0,250 L278,250 L328,160 L560,160" fill="none" stroke="var(--line-grey)" stroke-width="5"/>
      <path d="M0,292 L560,292 V320 H0 Z" fill="var(--band-light)"/>
    </svg>

    <div class="brand"><span class="brand__mark"></span>Venaza Coatings</div>

    <ul class="contact">
      <li class="contact__item">
        <span class="contact__icon">
          <svg width="16" height="16" viewBox="0 0 16 16"><circle cx="8" cy="5" r="3" fill="#fff"/><path d="M2,15 C2,10 14,10 14,15 Z" fill="#fff"/></svg>
        </span>
        Rodrigo Venaza
      </li>
      <li class="contact__item">
        <span class="contact__icon">
          <svg width="16" height="16" viewBox="0 0 16 16"><path d="M4,2 L6.5,2 L7.5,5 L6,6.2 C6.8,8 8,9.2 9.8,10 L11,8.5 L14,9.5 L14,12 C14,13 13,14 12,14 C7,14 2,9 2,4 C2,3 3,2 4,2 Z" fill="#fff"/></svg>
        </span>
        801-437-2916
      </li>
      <li class="contact__item">
        <span class="contact__icon">
          <svg width="16" height="16" viewBox="0 0 16 16"><rect x="2" y="4" width="12" height="8" fill="none" stroke="#fff" stroke-width="1.4"/><path d="M2,4 L8,9 L14,4" fill="none" stroke="#fff" stroke-width="1.4"/></svg>
        </span>
        Venazacoatings.utah@brushmail.net
      </li>
    </ul>

    <div class="services">
      <h2 class="services__title">SERVICES</h2>
      <div class="services__cols">
        <ul class="services__col services__col--left">
          <li>Interior &amp; Exterior</li>
          <li>Custom Paint &amp; Stain</li>
          <li>Log Staining and Refinishing</li>
        </ul>
        <ul class="services__col services__col--right">
          <li>Cabinet Refinishing</li>
          <li>Epoxy Coatings/</li>
          <li>Garage Floors</li>
        </ul>
      </div>
    </div>
  </section>

  <section class="card card--back" aria-label="Business card back">
    <svg class="card__bands" viewBox="0 0 560 320" aria-hidden="true">
      <rect x="0" y="240" width="560" height="12" fill="var(--stripe-dark)"/>
      <rect x="0" y="258" width="560" height="4" fill="var(--stripe-mid)"/>
      <rect x="0" y="268" width="560" height="52" fill="var(--stripe-base)"/>
      <rect x="0" y="284" width="560" height="3" fill="var(--stripe-mid)"/>
    </svg>
    <div class="brand"><span class="brand__mark"></span>Venaza Coatings</div>
  </section>

</body>
</html>
```